Meadowgale Equine Hemp horse feed supplement LABEL

Design a label for a horse feed supplement made from hemp. American grown hemp, American made product, American owned company. This is targeted towards the race horse market, so a race horse graphic would be ideal.

Our slogan "The foundation of equine vitality"

**When adding our logo, please change the lime green in our logo to #c1df7f **
Give TWO label options with the logo as described above and also an option with the word Equine removed from our logo.**
Updates

Target Market(s)

Performance Horses (Racing, team roping, cutting, reining, jumping)

Industry/Entity Type

Horseback Riding

Colors
eaf2ce
cadf82

Requirements
Must have
• - Meadowgale Equine Logo AS DESCRIBED in project description
- Checkboxes at the bottom with different size package choice (1lb, 5lb, 10lb, 25lb, 50lb) - We will hand mark the size when packaging

The following benefits of CBD:
- Anti-Inflammatory
- Pain Relief
- Anti-Anxiety
- Acid Neutralizer

Dosing Instructions:
750mg - Gastric care, joint support, inflammation, arthritis, and stress (1/2 Scoop)
1500mg - Chronic pain, seizures, severe arthritis, and intense anxiety (Full scoop)

Ingredients: Cannabis Sativa (Hemp)
Nice to have
• Would like to be able to stick a QR code on the label that will change between batches of hemp.

```html
<!DOCTYPE html>
<html lang="en">
<head>
<meta charset="utf-8">
<title>Meadowgale Equine Hemp – Label Options</title>
<link href="https://fonts.googleapis.com/css2?family=Cinzel:wght@400;600;700&family=Montserrat:wght@400;500;600;700&display=swap" rel="stylesheet">
<style>
  :root{
    --backdrop:#b4b4b4;
    --paper:#ffffff;
    --paper-shade:#f1f1f1;
    --brown:#4b3a30;
    --brown-deep:#3a2b22;
    --lime:#c1df7f;
    --lime-text:#a9cc62;
    --lime-pale:#eaf2ce;
    --ink:#2a1c15;
    --light-text:#f4efe9;
  }
  *{box-sizing:border-box;margin:0;padding:0}
  html,body{width:1200px;height:835px;overflow:hidden}
  body{background:var(--backdrop);font-family:"Montserrat",sans-serif;position:relative}

  .label{
    position:absolute;top:120px;width:326px;height:572px;
    background:linear-gradient(180deg,var(--paper-shade) 0,var(--paper) 14%,var(--paper) 88%,var(--paper-shade) 100%);
    border-radius:10px;overflow:hidden;text-align:center;color:var(--ink);
  }
  .label--full{left:300px}
  .label--half{left:720px}

  .zip-line{position:absolute;left:14px;right:14px;height:2px;background:#e2e2e2}
  .zip-line--a{top:58px}.zip-line--b{top:66px}

  .brand-band{
    position:absolute;top:90px;left:0;right:0;height:84px;
    background:var(--brown);border-radius:0 0 50% 50% / 0 0 20px 20px;
    display:flex;flex-direction:column;align-items:center;justify-content:flex-end;padding-bottom:10px;
  }
  .brand-name{
    display:flex;align-items:center;gap:6px;
    font-family:"Cinzel",serif;font-weight:600;font-size:22px;color:var(--light-text);letter-spacing:.5px;
  }
  .brand-dot{width:9px;height:9px;border-radius:50%;background:var(--lime)}
  .slogan{margin-top:7px;font-family:"Cinzel",serif;font-weight:700;font-size:8.6px;color:var(--lime);letter-spacing:.2px}

  .species{position:absolute;top:180px;left:0;right:0;font-family:"Cinzel",serif;font-size:17px;line-height:20px;color:var(--lime-text);letter-spacing:.5px}
  .product{position:absolute;top:204px;left:0;right:0;font-family:"Cinzel",serif;font-weight:700;font-size:50px;line-height:46px;color:var(--brown-deep);letter-spacing:-1px}
  .audience{position:absolute;top:253px;left:0;right:0;font-weight:600;font-size:12px;line-height:14px;color:var(--brown-deep);letter-spacing:.6px}
  .disciplines{position:absolute;top:269px;left:0;right:0;font-size:7.6px;line-height:10px;font-weight:600;color:var(--lime-text)}

  .racehorse-art{
    position:absolute;top:283px;left:70px;width:190px;height:100px;
    background:radial-gradient(ellipse at 55% 55%,#8a7467 0,#d9d0c9 55%,var(--paper) 78%);
    border-radius:40%;
  }

  .dosing-band{
    position:absolute;top:386px;left:18px;right:18px;height:18px;
    background:linear-gradient(180deg,var(--lime) 0,var(--lime-pale) 100%);
    font-family:"Cinzel",serif;font-weight:700;font-size:7.6px;line-height:19px;color:var(--brown-deep);
  }
  .dosing-list{
    position:absolute;top:410px;left:20px;right:20px;
    display:flex;justify-content:space-between;font-size:4.6px;font-weight:600;color:var(--brown-deep);
  }
  .dosing-list li{list-style:none}
  .dosing-list li::before{content:"• "}

  .size-title{position:absolute;top:431px;left:0;right:0;font-size:10.5px;line-height:13px;font-weight:500;letter-spacing:1.4px;color:var(--brown-deep)}
  .size-options{position:absolute;top:449px;left:50px;right:30px;display:flex;justify-content:space-between}
  .size-option{display:flex;align-items:center;gap:3px;font-size:8px;font-weight:600;color:var(--lime-text)}
  .size-option svg{display:block}

  .benefits-band{
    position:absolute;top:462px;left:0;right:0;height:86px;background:var(--brown);
    border-radius:50% 50% 0 0 / 6px 6px 0 0;color:var(--light-text);
  }
  .benefits-title{margin-top:12px;font-size:10px;line-height:12px;font-weight:700;letter-spacing:.8px}
  .benefits-list{
    list-style:none;display:grid;grid-template-columns:1fr 1fr;row-gap:6px;
    text-align:left;padding:8px 30px 0 46px;font-size:7px;line-height:9px;letter-spacing:.4px;
  }
  .benefits-list li::before{content:"• ";font-size:8px}

  .net-weight{
    position:absolute;top:534px;left:50%;transform:translateX(-50%);
    background:var(--paper);border-radius:5px;padding:3px 6px;
    font-size:8px;line-height:10px;font-weight:700;color:var(--brown-deep);white-space:nowrap;
  }
</style>
</head>
<body>

<svg width="0" height="0" style="position:absolute" aria-hidden="true">
  <symbol id="checkbox" viewBox="0 0 11 11"><rect x=".6" y=".6" width="9.8" height="9.8" fill="none" stroke="#3a2b22" stroke-width="1"/></symbol>
</svg>

<article class="label label--full">
  <div class="zip-line zip-line--a"></div><div class="zip-line zip-line--b"></div>
  <header class="brand-band">
    <div class="brand-name"><span class="brand-dot"></span>Meadowgale</div>
    <p class="slogan">THE FOUNDATION OF EQUINE VITALITY</p>
  </header>
  <p class="species">CANNABIS SATIVA</p>
  <h1 class="product">HEMP</h1>
  <p class="audience">PERFORMANCE HORSES</p>
  <p class="disciplines">(Racing, team roping, cutting, reining, jumping)</p>
  <div class="racehorse-art" role="img" aria-label="Brown line illustration of a galloping racehorse with jockey"></div>
  <div class="dosing-band">DOSING INSTRUCTIONS:</div>
  <ul class="dosing-list"><li>GASTRIC CARE</li><li>JOINT SUPPORT</li><li>ARTHRITIS</li><li>INFLAMMATION</li><li>STRESS (1/2 SCOOP)</li></ul>
  <p class="size-title">DIFFERENT SIZE PACKAGE CHOICE</p>
  <div class="size-options">
    <span class="size-option">1LB<svg width="11" height="11"><use href="#checkbox"/></svg></span>
    <span class="size-option">5LB<svg width="11" height="11"><use href="#checkbox"/></svg></span>
    <span class="size-option">10LB<svg width="11" height="11"><use href="#checkbox"/></svg></span>
    <span class="size-option">25LB<svg width="11" height="11"><use href="#checkbox"/></svg></span>
    <span class="size-option">50LB<svg width="11" height="11"><use href="#checkbox"/></svg></span>
  </div>
  <section class="benefits-band">
    <h2 class="benefits-title">BENEFITS OF CBD:</h2>
    <ul class="benefits-list"><li>ANTI-INFLAMMATORY</li><li>PAIN RELIEF</li><li>ANTI-ANXIETY</li><li>ACID NEUTRALIZER</li></ul>
  </section>
  <p class="net-weight">NET WET:1500mg</p>
</article>

<article class="label label--half">
  <div class="zip-line zip-line--a"></div><div class="zip-line zip-line--b"></div>
  <header class="brand-band">
    <div class="brand-name"><span class="brand-dot"></span>Meadowgale</div>
    <p class="slogan">THE FOUNDATION OF EQUINE VITALITY</p>
  </header>
  <p class="species">CANNABIS SATIVA</p>
  <h1 class="product">HEMP</h1>
  <p class="audience">PERFORMANCE HORSES</p>
  <p class="disciplines">(Racing, team roping, cutting, reining, jumping)</p>
  <div class="racehorse-art" role="img" aria-label="Brown line illustration of a galloping racehorse with jockey"></div>
  <div class="dosing-band">DOSING INSTRUCTIONS:</div>
  <ul class="dosing-list"><li>GASTRIC CARE</li><li>JOINT SUPPORT</li><li>ARTHRITIS</li><li>INFLAMMATION</li><li>STRESS (1/2 SCOOP)</li></ul>
  <p class="size-title">DIFFERENT SIZE PACKAGE CHOICE</p>
  <div class="size-options">
    <span class="size-option">1LB<svg width="11" height="11"><use href="#checkbox"/></svg></span>
    <span class="size-option">5LB<svg width="11" height="11"><use href="#checkbox"/></svg></span>
    <span class="size-option">10LB<svg width="11" height="11"><use href="#checkbox"/></svg></span>
    <span class="size-option">25LB<svg width="11" height="11"><use href="#checkbox"/></svg></span>
    <span class="size-option">50LB<svg width="11" height="11"><use href="#checkbox"/></svg></span>
  </div>
  <section class="benefits-band">
    <h2 class="benefits-title">BENEFITS OF CBD:</h2>
    <ul class="benefits-list"><li>ANTI-INFLAMMATORY</li><li>PAIN RELIEF</li><li>ANTI-ANXIETY</li><li>ACID NEUTRALIZER</li></ul>
  </section>
  <p class="net-weight">NET WET:750mg</p>
</article>

</body>
</html>
```